Skyvanterra.com

My website is a kind of blog, about drones and UAVs. Now I want to add another part where A guite to UAV/Drone companies will show up and ad space will be needed. I have now, name and address of many, maybe most of such a companies. What I'd like is a new page design for this purpose. I hope I let me understood.
Updates

Hello Designers. I think that none of you have understood what I asked for. What I want is a Drone-Directory Template page which be added to SkyvanTerra.com on a WP base. Anyone of you has viewed a Amber Leaf Registry? Well that is what I want. An elegant Directory web page. I'll put on the page drone manufacturers name, address, email and one or many ads as you've seen on a Amber Leafs Registry. Don't forget that this page will be used as a WP Template. Regards Marcelo

Hi, I would like to extend this project for one more week since none of designers undestood what I want althogh I've sent messages clarifying to some of them. Please tell me what next steps will be.

Reason: I would like to extend deadline for 7 more days. Once accepted by designers, I will explain them again what is what I want.

Target Market(s)

Customers will be people engaged in the drine business. Ages 19-65. Mos of the will be English speaking. Most of them own drone manufacture pr drone distribution business.
People liking speed, photography, farming, rescue, investigation and so on.

Font styles to use
Serif
Sans Serif

Requirements
Must have
• Think it is a guide. There should be lines, an abc... Too. And also think that, as any other guide, there will be people interested in shoeing up more by means of advertisements. So,lace for ads are a must.
Nice to have
• Logo ahould show a flying srone
Should not have
• Not old style.Modern fonts, no money bag illustrations.

```html
<!DOCTYPE html>
<html lang="en">
<head>
<meta charset="utf-8">
<title>Skyvanterra – Drone Directory</title>
<link href="https://fonts.googleapis.com/css2?family=Open+Sans:wght@400;600;700&family=Oswald:wght@300;400&display=swap" rel="stylesheet">
<style>
:root{
  --navy-deep:#1c1f5e;
  --navy-glow:#3a4fa8;
  --cyan:#1fb0d6;
  --ink:#333840;
  --muted:#8a8f96;
  --line:#e3e5e8;
  --panel:#ffffff;
  --band:#e5e5e5;
  --footer:#2e3a50;
  --star:#f4c21b;
  --button-grey:#6d6f73;
}
*{box-sizing:border-box;margin:0;padding:0}
html,body{width:872px;height:1200px;overflow:hidden}
body{position:relative;background:#fff;font-family:"Open Sans",Arial,sans-serif;color:var(--ink)}
.abs{position:absolute}

/* Header */
.site-header{left:0;top:0;width:872px;height:258px;
  background:radial-gradient(ellipse 260px 150px at 436px 110px,#4a6cc4 0%,#2f3d93 45%,var(--navy-deep) 100%)}
.brand{left:36px;top:36px;font-family:"Oswald",sans-serif;font-weight:300;font-size:28px;letter-spacing:2px;color:var(--cyan);text-transform:uppercase}
.main-nav{top:38px;left:0;width:872px;font-family:"Oswald",sans-serif;font-size:14px;color:#fff}
.main-nav a{position:absolute;color:#fff;text-decoration:none;white-space:nowrap}
.main-nav a.active{color:var(--cyan)}
.search-title{left:0;width:872px;top:112px;text-align:center;color:#fff;font-weight:700;font-size:22px;letter-spacing:1px}
.search-box{left:290px;top:150px;width:292px;height:31px;background:#fff;border-radius:5px;font-size:12px;color:#999;padding:8px 12px}
.search-box svg{position:absolute;right:12px;top:5px}

/* Panels */
.panel{background:var(--panel);box-shadow:0 1px 4px rgba(0,0,0,.18)}
.panel-head{display:flex;align-items:center;gap:10px;font-size:13px;font-weight:600;color:#444}
.panel-head .icon{width:18px;height:18px;background:#2f3543;border-radius:2px;display:flex;align-items:center;justify-content:center}

.categories{left:40px;top:248px;width:223px;height:370px}
.categories .panel-head{position:absolute;left:18px;top:22px}
.categories .rule{position:absolute;left:18px;top:49px;width:194px;border-top:1px solid #ccc}
.cat-list{position:absolute;left:18px;top:52px;width:194px;list-style:none}
.cat-list li{height:29.5px;border-bottom:1px solid var(--line);display:flex;justify-content:space-between;align-items:center;font-size:11px;color:#555;padding-right:14px}
.cat-list li:last-child{border-bottom:none}
.cat-list li.active{color:var(--cyan)}
.cat-list li span{font-size:9px;color:#777}

/* Slider */
.hero-slide{left:302px;top:248px;width:532px;height:182px;border:3px solid var(--cyan);background:#fff;box-shadow:0 8px 10px -6px rgba(0,0,0,.35)}
.slide-media{left:12px;top:13px;width:250px;height:150px;background:radial-gradient(ellipse at center,#d8d8d2 0%,#f3f3f0 60%,#fff 100%)}
.slide-title{left:274px;top:28px;font-size:13px;font-weight:600;color:var(--cyan);text-transform:uppercase}
.slide-text{left:274px;top:50px;width:240px;font-size:9px;line-height:15px;color:#777}
.btn-grey{left:274px;top:122px;width:73px;height:23px;background:var(--button-grey);color:#fff;font-size:9px;display:flex;align-items:center;justify-content:center}
.slide-arrow{width:23px;height:32px;background:var(--cyan);display:flex;align-items:center;justify-content:center}

/* Business search */
.business{left:302px;top:452px;width:532px;height:166px}
.business .panel-head{position:absolute;left:20px;top:24px}
.business .rule{position:absolute;left:20px;top:51px;width:210px;border-top:1px solid #ccc}
.btn-cyan{background:var(--cyan);color:#fff;font-size:9px;font-weight:600;display:flex;align-items:center;justify-content:center}
.biz-col{list-style:none;font-size:10px;color:#666;top:74px}
.biz-col li{height:19.5px;white-space:nowrap}
.biz-col li b{font-weight:400;color:#999;font-size:8px;margin-right:6px}
.biz-col li.active{color:var(--cyan)}

/* Featured */
.featured{left:0;top:654px;width:872px;height:249px;background:var(--band)}
.section-title{width:872px;left:0;text-align:center;font-size:13px;font-weight:600;letter-spacing:.5px;text-transform:uppercase}
.listing{top:46px;width:167px;height:140px;background:#fff}
.listing .thumb{position:absolute;left:5px;top:5px;width:157px;height:82px}
.listing .name{position:absolute;left:5px;top:92px;font-size:9px;color:#555}
.listing .sub{position:absolute;left:5px;top:106px;font-size:8px;color:#aaa}
.listing .stars{position:absolute;left:5px;top:119px;display:flex;gap:1px}
.carousel-arrow{top:100px}

/* Testimonials */
.testimonials{left:0;top:903px;width:872px;height:232px;
  background:radial-gradient(ellipse 90px 70px at 490px 70px,#b98a3a 0%,rgba(120,110,60,0) 100%),
  linear-gradient(180deg,#2c2a24 0%,#3d4a30 45%,#4c6a34 70%,#3a4e2a 100%)}
.testimonials .section-title{color:#fff;top:30px}
.quote{left:160px;top:70px;width:552px;text-align:center;color:#fff;font-size:9px;line-height:15px}
.client{left:0;width:872px;top:168px;text-align:center;color:#fff;font-size:10px;font-weight:600;text-transform:uppercase}
.dots{left:416px;top:204px;display:flex;gap:5px}
.dots i{width:9px;height:9px;border-radius:50%;background:#fff;display:block}
.dots i.on{background:var(--cyan)}

/* Footer */
.site-footer{left:0;top:1135px;width:872px;height:65px;background:var(--footer)}
.copyright{left:72px;top:24px;font-size:10px;color:#fff}
.copyright a{color:var(--cyan);text-decoration:none}
.social{left:742px;top:24px;display:flex;gap:12px}
.social i{display:block;width:16px;height:16px;border-radius:50%;background:#fff}
</style>
</head>
<body>

<header class="site-header abs">
  <div class="brand abs">Skyvanterra</div>
  <nav class="main-nav abs">
    <a class="active" style="left:596px">Home</a>
    <a style="left:654px">Classifieds</a>
    <a style="left:737px">Courses</a>
    <a style="left:808px">Log In</a>
  </nav>
  <h1 class="search-title abs">SEARCH</h1>
  <div class="search-box abs">I am looking for
    <svg width="22" height="22" viewBox="0 0 22 22"><circle cx="9" cy="9" r="6.5" fill="#e8f3fa" stroke="#7fa9c8" stroke-width="2"/><line x1="14" y1="14" x2="20" y2="20" stroke="#7fa9c8" stroke-width="3" stroke-linecap="round"/></svg>
  </div>
</header>

<aside class="categories panel abs">
  <div class="panel-head"><span class="icon"><svg width="11" height="9" viewBox="0 0 11 9"><path d="M0 1h4l1 1h6v7H0z" fill="#fff"/></svg></span>Categories</div>
  <div class="rule"></div>
  <ul class="cat-list">
    <li class="active">simply dummy text1<span>&gt;&gt;</span></li>
    <li>simply dummy text2<span>&gt;&gt;</span></li>
    <li>simply dummy text3<span>&gt;&gt;</span></li>
    <li>simply dummy text1<span>&gt;&gt;</span></li>
    <li>simply dummy text2<span>&gt;&gt;</span></li>
    <li>simply dummy text3<span>&gt;&gt;</span></li>
    <li>simply dummy text1<span>&gt;&gt;</span></li>
    <li>simply dummy text2<span>&gt;&gt;</span></li>
    <li>simply dummy text3<span>&gt;&gt;</span></li>
    <li>simply dummy text2<span>&gt;&gt;</span></li>
  </ul>
</aside>

<section class="hero-slide abs">
  <div class="slide-media abs" role="img" aria-label="Photo of a multirotor camera drone with yellow arms and landing gear"></div>
  <h2 class="slide-title abs">Lorem Ipsum is simply dummy text</h2>
  <p class="slide-text abs">It is a long established fact that a reader will be distracted by the readable content of a page when looking at its layout. The point of using Lorem Ipsum is that it has a more-or-less normal distribution of letters</p>
  <div class="btn-grey abs">LET'S GO!</div>
</section>
<div class="slide-arrow abs" style="left:292px;top:324px"><svg width="8" height="12" viewBox="0 0 8 12"><path d="M7 1L2 6l5 5" stroke="#fff" stroke-width="2" fill="none"/></svg></div>
<div class="slide-arrow abs" style="left:821px;top:324px"><svg width="8" height="12" viewBox="0 0 8 12"><path d="M1 1l5 5-5 5" stroke="#fff" stroke-width="2" fill="none"/></svg></div>

<section class="business panel abs">
  <div class="panel-head"><span class="icon"><svg width="11" height="11" viewBox="0 0 11 11"><circle cx="4.5" cy="4.5" r="3" fill="none" stroke="#fff" stroke-width="1.6"/><line x1="7" y1="7" x2="10" y2="10" stroke="#fff" stroke-width="1.8"/></svg></span>Business Search</div>
  <div class="rule"></div>
  <div class="btn-cyan abs" style="left:440px;top:22px;width:72px;height:23px">MORE ...</div>
  <ul class="biz-col abs" style="left:20px">
    <li class="active"><b>&gt;&gt;</b>Established</li><li><b>&gt;&gt;</b>Fact</li><li><b>&gt;&gt;</b>Drones</li><li><b>&gt;&gt;</b>Business Drones</li>
  </ul>
  <ul class="biz-col abs" style="left:143px">
    <li><b>&gt;&gt;</b>Established</li><li><b>&gt;&gt;</b>Fact</li><li><b>&gt;&gt;</b>Drones</li><li><b>&gt;&gt;</b>Business Drones</li>
  </ul>
  <ul class="biz-col abs" style="left:260px">
    <li><b>&gt;&gt;</b>Established</li><li><b>&gt;&gt;</b>Fact</li><li><b>&gt;&gt;</b>Drones</li><li><b>&gt;&gt;</b>Business Drones</li>
  </ul>
  <ul class="biz-col abs" style="left:383px">
    <li><b>&gt;&gt;</b>Established</li><li><b>&gt;&gt;</b>Fact</li><li><b>&gt;&gt;</b>Drones</li><li><b>&gt;&gt;</b>Business Drones</li>
  </ul>
</section>

<section class="featured abs">
  <h2 class="section-title abs" style="top:16px">Featured Listing</h2>
  <svg class="carousel-arrow abs" style="left:42px" width="14" height="24" viewBox="0 0 14 24"><path d="M12 2L3 12l9 10" stroke="#999" stroke-width="2" fill="none"/></svg>
  <svg class="carousel-arrow abs" style="left:818px" width="14" height="24" viewBox="0 0 14 24"><path d="M2 2l9 10-9 10" stroke="#999" stroke-width="2" fill="none"/></svg>

  <article class="listing abs" style="left:74px">
    <div class="thumb" role="img" aria-label="Photo of a drone flying against a bright cyan and white backdrop" style="background:linear-gradient(135deg,#6fd3ee,#d9f2f8 60%,#9fdcee)"></div>
    <div class="name">dummy text of the printing</div><div class="sub">and typesetting industry</div>
    <div class="stars"><svg width="50" height="9" viewBox="0 0 50 9"><g fill="var(--star)"><polygon id="s" points="4.5,0 5.6,3.2 9,3.3 6.3,5.4 7.3,8.7 4.5,6.7 1.7,8.7 2.7,5.4 0,3.3 3.4,3.2"/><use href="#s" x="10"/><use href="#s" x="20"/><use href="#s" x="30"/><use href="#s" x="40"/></g></svg></div>
  </article>
  <article class="listing abs" style="left:259px">
    <div class="thumb" role="img" aria-label="Photo of drone operators in safety vests in a park" style="background:linear-gradient(180deg,#4f6d3c,#6b8a4c 55%,#8a8d86)"></div>
    <div class="name">dummy text of the printing</div><div class="sub">and typesetting industry</div>
    <div class="stars"><svg width="50" height="9" viewBox="0 0 50 9"><g fill="var(--star)"><use href="#s"/><use href="#s" x="10"/><use href="#s" x="20"/><use href="#s" x="30"/><use href="#s" x="40"/></g></svg></div>
  </article>
  <article class="listing abs" style="left:444px">
    <div class="thumb" role="img" aria-label="Photo of a black multirotor drone hovering over a city" style="background:linear-gradient(180deg,#c9c3bd,#a9a29a 60%,#d8d4cf)"></div>
    <div class="name">dummy text of the printing</div><div class="sub">and typesetting industry</div>
    <div class="stars"><svg width="50" height="9" viewBox="0 0 50 9"><g fill="var(--star)"><use href="#s"/><use href="#s" x="10"/><use href="#s" x="20"/><use href="#s" x="30"/><use href="#s" x="40"/></g></svg></div>
  </article>
  <article class="listing abs" style="left:632px">
    <div class="thumb" role="img" aria-label="Photo of a drone above a crowd at an event" style="background:linear-gradient(160deg,#3d4a2e,#6a5a3a 50%,#2e2a26)"></div>
    <div class="name">dummy text of the printing</div><div class="sub">and typesetting industry</div>
    <div class="stars"><svg width="50" height="9" viewBox="0 0 50 9"><g fill="var(--star)"><use href="#s"/><use href="#s" x="10"/><use href="#s" x="20"/><use href="#s" x="30"/><use href="#s" x="40"/></g></svg></div>
  </article>

  <div class="btn-cyan abs" style="left:400px;top:208px;width:72px;height:22px;font-weight:400">VIEW ALL</div>
</section>

<section class="testimonials abs" role="img" aria-label="Blurred photo of a drone over a grassy field">
  <h2 class="section-title abs">Testimonials</h2>
  <p class="quote abs">“ It is a long established fact that a reader will be distracted by the readable content of a page when looking at its layout. The point of using Lorem Ipsum is that it has a more-or-less normal distribution of letters, as opposed to using 'Content here, content here', making it look like readable English. Many desktop publishing packages and web page editors now use Lorem Ipsum as their default model text, and a search for 'lorem ipsum' will uncover many web sites still in their infancy. ”</p>
  <div class="client abs">Client's Name</div>
  <div class="dots abs"><i class="on"></i><i></i><i></i></div>
</section>

<footer class="site-footer abs">
  <p class="copyright abs">All rights Reserved © <a>skyvanterra.com</a></p>
  <div class="social abs"><i></i><i></i><i></i><i></i></div>
</footer>

</body>
</html>
```